New Business Card Design

We would like to refresh our business cards and make them look better. We are an IT company specialising in Cloud Services, IT Managed Services, software and hardware. I have attached a PSD of our current design. Also attached our logo.
Updates

I have uploaded all new logos in EPS format.

Can you please edit all designs to include a job title for Marcus Hale, eg. General Manager

Industry/Entity Type

Software

Colors
ffffff

Requirements
Must have
• Please use white background.
Should not have
• Black background

```html
<!DOCTYPE html>
<html lang="en">
<head>
<meta charset="utf-8">
<title>Kestrel Systems — Business Card</title>
<link rel="stylesheet" href="https://fonts.googleapis.com/css2?family=Source+Sans+3:wght@400;600&display=swap">
<style>
  :root {
    --paper: #ffffff;
    --ink: #1f2529;
    --accent: #c0392b;
    --link: #3a669f;
    --rule: #8fa0b3;
    --edge: #d6d6d6;
    --shadow: rgba(0, 0, 0, 0.28);
  }
  * { margin: 0; padding: 0; box-sizing: border-box; }
  html, body {
    width: 1200px;
    height: 1000px;
    overflow: hidden;
    background: var(--paper);
  }
  body {
    position: relative;
    font-family: "Source Sans 3", "Helvetica Neue", Arial, sans-serif;
    color: var(--ink);
  }
  .card {
    position: absolute;
    width: 739px;
    height: 416px;
    background: var(--paper);
    border: 1px solid var(--edge);
    box-shadow: 6px 8px 8px var(--shadow);
  }
  .card--front { left: 103px; top: 62px; }
  .card--back { left: 345px; top: 546px; }

  .brand {
    position: absolute;
    display: flex;
    flex-direction: column;
    align-items: center;
  }
  .brand__dot {
    border-radius: 50%;
    background: var(--accent);
  }
  .brand__name {
    font-weight: 400;
    color: var(--ink);
    white-space: nowrap;
    text-transform: lowercase;
  }
  .card--front .brand { left: 37px; width: 232px; top: 100px; }
  .card--front .brand__dot { width: 66px; height: 66px; margin-bottom: 54px; }
  .card--front .brand__name { font-size: 24px; letter-spacing: 3px; }

  .card--back .brand { left: 0; width: 100%; top: 104px; }
  .card--back .brand__dot { width: 82px; height: 82px; margin-bottom: 76px; }
  .card--back .brand__name { font-size: 32px; letter-spacing: 4px; }

  .website {
    position: absolute;
    left: 0;
    width: 306px;
    top: 318px;
    text-align: center;
    font-size: 12px;
    letter-spacing: 3.2px;
    color: var(--ink);
  }
  .divider {
    position: absolute;
    left: 328px;
    top: 75px;
    width: 1px;
    height: 266px;
    background: var(--rule);
  }
  .person {
    position: absolute;
    right: 38px;
    top: 84px;
    text-align: right;
  }
  .person__name {
    font-size: 50px;
    font-weight: 600;
    line-height: 1;
    letter-spacing: -0.5px;
    color: var(--ink);
  }
  .person__title {
    margin-top: 4px;
    font-size: 16px;
    letter-spacing: 3.4px;
    color: var(--accent);
    text-transform: uppercase;
  }
  .contact {
    position: absolute;
    display: flex;
    align-items: center;
    color: var(--link);
    white-space: nowrap;
  }
  .contact__icon {
    flex: none;
    width: 24px;
    height: 24px;
    margin-right: 8px;
  }
  .contact--email { left: 388px; top: 266px; font-size: 23px; }
  .contact--email .contact__icon { margin-right: 12px; }
  .contact--office { left: 387px; top: 316px; font-size: 17px; }
  .contact--mobile { left: 563px; top: 316px; font-size: 17px; }
  .contact--office .contact__icon,
  .contact--mobile .contact__icon { width: 22px; height: 22px; }
</style>
</head>
<body>

<section class="card card--front" aria-label="Business card front">
  <div class="brand">
    <span class="brand__dot"></span>
    <span class="brand__name">kestrel systems</span>
  </div>
  <p class="website">www.kestrelit.com.au</p>

  <span class="divider"></span>

  <div class="person">
    <h1 class="person__name">Marcus Hale</h1>
    <p class="person__title">General Manager</p>
  </div>

  <p class="contact contact--email">
    <svg class="contact__icon" viewBox="0 0 24 24" aria-hidden="true">
      <circle cx="12" cy="12" r="12" fill="#c0392b"/>
      <rect x="6" y="8" width="12" height="8.5" rx="0.8" fill="none" stroke="#fff" stroke-width="1.4"/>
      <path d="M6.5 8.6 L12 12.8 L17.5 8.6" fill="none" stroke="#fff" stroke-width="1.4"/>
    </svg>
    mhale@kestrelit.com.au
  </p>

  <p class="contact contact--office">
    <svg class="contact__icon" viewBox="0 0 24 24" aria-hidden="true">
      <circle cx="12" cy="12" r="12" fill="#c0392b"/>
      <path d="M8.2 6.2c.5-.4 1.1-.3 1.4.2l1.3 2.1c.3.5.2 1-.2 1.4l-.8.7c.6 1.5 1.9 2.9 3.4 3.6l.8-.8c.4-.4 1-.4 1.4-.1l2 1.3c.5.3.6 1 .2 1.4l-1 1.1c-.6.6-1.5.8-2.3.5-3.4-1.3-6-3.9-7.3-7.3-.3-.8-.1-1.7.5-2.3z" fill="#fff"/>
    </svg>
    07 5550 1234
  </p>

  <p class="contact contact--mobile">
    <svg class="contact__icon" viewBox="0 0 24 24" aria-hidden="true">
      <circle cx="12" cy="12" r="12" fill="#c0392b"/>
      <rect x="8.3" y="5.5" width="7.4" height="13" rx="1.2" fill="none" stroke="#fff" stroke-width="1.4"/>
      <rect x="9.7" y="7.4" width="4.6" height="7.4" fill="#fff"/>
      <circle cx="12" cy="16.7" r="0.8" fill="#fff"/>
    </svg>
    0400 555 017
  </p>
</section>

<section class="card card--back" aria-label="Business card back">
  <div class="brand">
    <span class="brand__dot"></span>
    <span class="brand__name">kestrel systems</span>
  </div>
</section>

</body>
</html>
```